QSL Card

project is a QSL card for amateur radio operators - must radio show call sign predomiately and in large letters on the card - VK5RUT - then must say somewhere Greetings from Australia - must also include name, address, website and coordinates in small trype - Martin Keble,47 Birch Rd., Tarrowby SA 5170 Australia, http://www.martinkebleqsl.com, - Grid Square PF82kr, CQ Zone 30, ITU Zone 59 - must also have a long rectangular box down the bottom of the card with six boxes inside the long box that can be filled in showing a heading in each box --- in box 1 Confirming QSO with.... box 2 Date (Z) ....., box 3 UTC ...... box 4 Freq / 2XMode ...... box 5 Pwr Out,..... boxx 6 Report ..... use attached pictures in the design with the radio equiipment as a background and my photo superimposed somewhere -- and the other attached image shows how i want the box to look - and on the right hand side down the bottom in small letters - 73s, Tnx QSL Pse

Reason: none of the designs i received totally fit the bill - see my new brief and budget

hi all - i finally decided i didnt like any of the designs i received so i have increased the budget and extended the deadline - i have also updated my brief and added another picture

Target Market(s)

amateur radio operators

Industry/Entity Type

Radio

Colors

Designer to choose colors to be used in the design.

```html
<!DOCTYPE html>
<html lang="en">
<head>
<meta charset="utf-8">
<title>VK5RUT QSL Card</title>
<link rel="stylesheet" href="https://fonts.googleapis.com/css2?family=Roboto:wght@400;700;900&family=Open+Sans:wght@400;600;700&family=Tinos:wght@400&display=swap">
<style>
  :root {
    --stage: #4f4f4f;
    --stage-edge: #3f3f3f;
    --navy-deep: #1a2550;
    --navy: #2a3a72;
    --navy-light: #34488a;
    --field: #ffffff;
    --label: #e8ecf7;
    --muted: #a9bbe4;
    --paper: #ffffff;
    --rule: #d9d9d9;
    --stamp: #dcdcdc;
    --ink: #333333;
  }
  * { box-sizing: border-box; margin: 0; padding: 0; }
  html, body { width: 1200px; height: 530px; overflow: hidden; }
  body {
    background: radial-gradient(ellipse at center, var(--stage) 0%, var(--stage-edge) 100%);
    font-family: "Open Sans", Arial, sans-serif;
    position: relative;
  }
  .card {
    position: absolute;
    top: 76px;
    width: 491px;
    height: 379px;
    box-shadow: 0 6px 18px rgba(0,0,0,0.45);
  }
  .card-front { left: 93px; }
  .shack-photo {
    width: 100%; height: 100%;
    background:
      linear-gradient(180deg, rgba(150,120,100,0.55) 0%, rgba(90,80,75,0.3) 40%, rgba(40,40,45,0.7) 100%),
      linear-gradient(90deg, #8a5a3c 0%, #6e6058 35%, #3a3a3e 70%, #505258 100%);
  }
  .card-back { left: 620px; display: flex; }
  .details {
    position: relative;
    width: 263px; height: 100%;
    background:
      radial-gradient(ellipse 45% 12% at 62% 6%, rgba(140,180,255,0.5), transparent 70%),
      linear-gradient(180deg, var(--navy-deep) 0%, var(--navy) 50%, var(--navy-light) 100%);
    color: var(--label);
    overflow: hidden;
  }
  .greeting {
    position: absolute; top: 8px; left: 0; width: 100%;
    text-align: center; font-family: "Tinos", "Times New Roman", serif;
    font-size: 9px; letter-spacing: 1px; color: var(--muted);
  }
  .callsign {
    position: absolute; top: 16px; left: 0; width: 100%;
    text-align: center;
    font-family: "Roboto", Arial, sans-serif;
    font-weight: 900; font-size: 58px; line-height: 68px; letter-spacing: -1px;
    background: linear-gradient(180deg, #ffffff 0%, #e6ebf5 55%, #9aa8c4 100%);
    -webkit-background-clip: text; background-clip: text; color: transparent;
  }
  .operator {
    position: absolute; top: 87px; left: 0; width: 100%;
    text-align: center; font-weight: 700; font-size: 16px; line-height: 20px; color: #fff;
  }
  .address, .website, .station-data {
    position: absolute; left: 0; width: 100%;
    text-align: center; font-family: "Tinos", "Times New Roman", serif;
    color: var(--muted); white-space: nowrap;
  }
  .address { top: 107px; font-size: 9.5px; line-height: 12px; }
  .website { top: 119px; font-size: 9.5px; line-height: 12px; }
  .station-data { top: 132px; font-size: 7.5px; line-height: 10px; }
  .log-fields { position: absolute; top: 149px; left: 0; width: 100%; }
  .field {
    position: absolute; left: 0; width: 100%; height: 21px;
    display: flex; align-items: center;
  }
  .field-label {
    width: 72px; text-align: right;
    font-family: "Tinos", "Times New Roman", serif;
    font-size: 10px; line-height: 11px; color: var(--label);
  }
  .field-box {
    position: absolute; left: 83px; width: 165px; height: 21px;
    background: var(--field); border-radius: 4px;
    box-shadow: inset 0 1px 2px rgba(0,0,0,0.25);
  }
  .sign-off {
    position: absolute; top: 358px; left: 0; width: 100%;
    text-align: center; font-size: 8.5px; line-height: 12px; color: var(--muted);
  }
  .address-side {
    position: relative; flex: 1; height: 100%; background: var(--paper);
  }
  .stamp-box {
    position: absolute; top: 28px; right: 29px; width: 60px; height: 71px;
    border: 6px solid var(--stamp);
    display: flex; align-items: center; justify-content: center;
    text-align: center; font-size: 6px; line-height: 10px; color: var(--ink);
    font-family: "Roboto", Arial, sans-serif;
  }
  .to-label {
    position: absolute; top: 151px; left: 15px; font-size: 9px; color: var(--ink);
  }
  .address-line {
    position: absolute; left: 15px; right: 31px; height: 1px; background: var(--rule);
  }
</style>
</head>
<body>
  <div class="card card-front">
    <div class="shack-photo" role="img" aria-label="Photograph of an amateur radio shack: stacked transceivers, a monitor and keyboard on a desk, with collected QSL cards on a brick wall"></div>
  </div>

  <div class="card card-back">
    <div class="details">
      <div class="greeting">GREETINGS FROM AUSTRALIA</div>
      <div class="callsign">VK5RUT</div>
      <div class="operator">Martin Keble</div>
      <div class="address">47 Birch Rd., Tarrowby SA 5170 Australia</div>
      <div class="website">www.martinkebleqsl.com</div>
      <div class="station-data">Grid Square PF82kr · CQ Zone 30 · ITU Zone 59</div>

      <div class="log-fields">
        <div class="field" style="top:0px"><span class="field-label">Confirming<br>QSO</span><span class="field-box"></span></div>
        <div class="field" style="top:35px"><span class="field-label">date (Z)</span><span class="field-box"></span></div>
        <div class="field" style="top:70px"><span class="field-label">UTC</span><span class="field-box"></span></div>
        <div class="field" style="top:105px"><span class="field-label">Freq /<br>2XMode</span><span class="field-box"></span></div>
        <div class="field" style="top:140px"><span class="field-label">pwr Out</span><span class="field-box"></span></div>
        <div class="field" style="top:174px"><span class="field-label">Report</span><span class="field-box"></span></div>
      </div>

      <div class="sign-off">73, Tnx QSL Pse</div>
    </div>

    <div class="address-side">
      <div class="stamp-box">PLEASE<br>PLACE<br>STAMP<br>HERE</div>
      <div class="to-label">To.</div>
      <div class="address-line" style="top:185px"></div>
      <div class="address-line" style="top:216px"></div>
      <div class="address-line" style="top:247px"></div>
      <div class="address-line" style="top:279px"></div>
      <div class="address-line" style="top:310px"></div>
    </div>
  </div>
</body>
</html>
```